Plastic Business Card for Bookkeeper

We are looking for a simple professional business card design to use for printing on thin frosted plastic (see-through) card stock. Logo and brand guideline documents are attached as well as a photo of our old business card, and another business card example that we like.

Target Market(s)

Small Business

Industry/Entity Type

Bookkeeper

Contact Information for Business Card

Harriet Valdez CPA
Chief Executive Bookkeeper
T. 03 5926 4187
M. 0432 861 507
E. harriet@quillpathledger.com
W. www.quillpathledger.com

Font styles to use
Sans Serif

Colors
6b449b
00a990

Requirements
Must have
• Stick with logo colors. Writing should be clear and easy to read and not too cramped together.
Nice to have
• Tag line for back of the card - 'Not your ordinary Bookkeeper'

```html
<!DOCTYPE html>
<html lang="en">
<head>
<meta charset="utf-8">
<title>Quillpath Ledger – Business Card</title>
<link href="https://fonts.googleapis.com/css2?family=Roboto:wght@400;500&display=swap" rel="stylesheet">
<style>
  :root {
    --teal: #007a8c;
    --purple: #6b449b;
    --ink: #4f4f4f;
    --frost: #ead3b0;
    --backdrop: #efe9e1;
    --white: #ffffff;
  }
  * { margin: 0; padding: 0; box-sizing: border-box; }
  html, body {
    width: 1190px; height: 1200px; overflow: hidden;
    background: var(--backdrop);
    font-family: "Roboto", Arial, sans-serif;
  }
  .canvas { position: relative; width: 1190px; height: 1200px; }

  .card {
    position: absolute; left: 241px; width: 696px; height: 394px;
    border-radius: 24px; overflow: hidden;
    box-shadow: 0 6px 18px rgba(0,0,0,0.18);
  }
  .card--front { top: 155px; background: var(--frost); }
  .card--back  { top: 660px; background: var(--teal); }

  /* Front */
  .brand { position: absolute; left: 62px; top: 40px; width: 170px; text-align: center; }
  .brand__dot { display: block; width: 64px; height: 64px; margin: 0 auto 22px; border-radius: 50%; background: var(--teal); }
  .brand__name { color: var(--purple); font-weight: 500; font-size: 17px; letter-spacing: 0.8px; line-height: 23px; }

  .contact { position: absolute; left: 68px; top: 257px; list-style: none; }
  .contact li { display: flex; align-items: center; height: 20px; color: var(--ink); font-size: 15px; }
  .contact svg { width: 13px; height: 13px; margin-right: 11px; fill: var(--teal); flex: none; }

  .person { position: absolute; right: 77px; top: 275px; text-align: right; }
  .person__name { color: var(--teal); font-weight: 500; font-size: 24px; line-height: 28px; }
  .person__role { color: var(--purple); font-weight: 500; font-size: 16.5px; line-height: 20px; }
  .person__pointer { position: absolute; right: 0; top: 269px; width: 52px; height: 42px; }

  /* Back */
  .back-brand { position: absolute; left: 0; right: 0; top: 120px; text-align: center; }
  .back-brand__dot { display: block; width: 110px; height: 110px; margin: 0 auto 22px; border-radius: 50%; border: 7px solid var(--white); }
  .back-brand__name { color: var(--white); font-weight: 500; font-size: 26px; letter-spacing: 1px; }
  .back-url { position: absolute; left: 0; right: 0; top: 338px; text-align: center; color: var(--white); font-size: 17.5px; }
</style>
</head>
<body>
<main class="canvas">
  <section class="card card--front">
    <div class="brand">
      <span class="brand__dot"></span>
      <div class="brand__name">QUILLPATH<br>LEDGER</div>
    </div>

    <ul class="contact">
      <li><svg viewBox="0 0 24 24"><path d="M6.6 10.8a15 15 0 0 0 6.6 6.6l2.2-2.2a1 1 0 0 1 1-.25 11.4 11.4 0 0 0 3.6.57 1 1 0 0 1 1 1V20a1 1 0 0 1-1 1A17 17 0 0 1 3 4a1 1 0 0 1 1-1h3.5a1 1 0 0 1 1 1c0 1.25.2 2.45.57 3.57a1 1 0 0 1-.25 1z"/></svg>03 5926 4187</li>
      <li><svg viewBox="0 0 24 24"><path d="M7 1h10a2 2 0 0 1 2 2v18a2 2 0 0 1-2 2H7a2 2 0 0 1-2-2V3a2 2 0 0 1 2-2zm0 3v14h10V4z"/></svg>0432 861 507</li>
      <li><svg viewBox="0 0 24 24"><path d="M2 5h20v14H2zm2 2v.5l8 5 8-5V7zm0 2.8V17h16V9.8l-8 5z"/></svg>harriet@quillpathledger.com</li>
      <li><svg viewBox="0 0 24 24"><path d="M12 2a10 10 0 1 0 0 20 10 10 0 0 0 0-20zm-1 17.9A8 8 0 0 1 4.2 10L9 14.8v1a2 2 0 0 0 2 2zm6.9-2.5A2 2 0 0 0 16 16h-1v-3a1 1 0 0 0-1-1H8v-2h2a1 1 0 0 0 1-1V7h2a2 2 0 0 0 2-2v-.4a8 8 0 0 1 2.9 12.8z"/></svg>www.quillpathledger.com</li>
    </ul>

    <div class="person">
      <div class="person__name">Harriet Valdez CPA</div>
      <div class="person__role">Chief Executive Bookkeeper</div>
    </div>
    <svg class="person__pointer" viewBox="0 0 52 42" aria-hidden="true"><polygon points="0,24 52,0 52,42" fill="var(--teal)"/></svg>
  </section>

  <section class="card card--back">
    <div class="back-brand">
      <span class="back-brand__dot"></span>
      <div class="back-brand__name">QUILLPATH LEDGER</div>
    </div>
    <div class="back-url">www.quillpathledger.com</div>
  </section>
</main>
</body>
</html>
```